Tidewell Shuck-new seafood raw bar restaurant menu

We are a Local Seafood & Raw Bar restaurant that is looking to open in 3 months. I need-Dinner Menu Design, Happy Hour Menu, Cocktail Menu, Brunch Menu, Lunch Menu. I'd like to have you start w/ the dinner menu first then whomever I choose will also do the rest of my menus. The OYSTERDECK by Finnhook menu is the direction im going for as far as font organization. Id like you to give us our own personal touch. Ive also provided a mock menu that a local designer started that can't finish due to timing.

Target Market(s)

mid to high end casual seafood restaurant

Industry/Entity Type

restaurant

Font styles to use
Serif
Sans Serif

Colors
0054AA
0677BA
7BADD7
CADEEF
E8F1F8
0094D4
00A9DD
6FCCEA
C7EBF8
E9F6FB
00AB8E
00BBA5
67D7C9
C6EFE9
E9F9F6

Requirements
Must have
• 11" x 14" size

```html
<!DOCTYPE html>
<html lang="en">
<head>
<meta charset="utf-8">
<title>Tidewell Shuck – Dinner Menu</title>
<link rel="stylesheet" href="https://fonts.googleapis.com/css2?family=Arvo:wght@700&family=Lato:ital,wght@0,700;1,400;1,700;1,900&display=swap">
<style>
  :root{
    --page:#eef0f3;
    --navy:#2d5795;
    --navy-deep:#1c3a6b;
    --ink:#1f3560;
    --frame:#e9f1f8;
    --sky:#cadeef;
    --sky-pale:#e9f6fb;
    --cyan:#6fccea;
    --cyan-bright:#7fd6f2;
    --orange-a:#f4511e;
    --orange-b:#ffa51f;
    --white:#ffffff;
    --slab:"Arvo", Georgia, serif;
    --sans:"Lato", Arial, sans-serif;
  }
  *{box-sizing:border-box;margin:0;padding:0}
  html,body{width:1200px;height:692px;overflow:hidden;background:var(--page)}
  .menu-sheet{
    position:absolute;left:125px;top:5px;width:1092px;height:783px;
    background:var(--navy);transform:scale(.87);transform-origin:0 0;
    font-family:var(--sans);color:var(--white);
  }
  .frame-outer{position:absolute;left:18px;top:21px;width:1052px;height:735px;border:2px solid var(--frame)}
  .frame-inner{position:absolute;left:33px;top:38px;width:1019px;height:700px;border:1px solid var(--frame)}
  .menu-script{position:absolute;left:55px;top:56px;width:245px;height:114px;border-radius:40px;background:rgba(255,255,255,.85)}
  .brand-mark{position:absolute;left:378px;top:60px;width:62px;height:62px;border-radius:50%;background:var(--white)}
  .brand-name{position:absolute;left:456px;top:52px;font:700 34px/1 var(--slab);letter-spacing:1px;color:var(--white);white-space:nowrap}
  .brand-sub{position:absolute;left:456px;top:96px;font:700 21px/1 var(--slab);letter-spacing:1.5px;color:var(--cyan);white-space:nowrap}
  .brand-rule{position:absolute;left:456px;top:90px;width:266px;border-top:1px dashed var(--white)}
  .service-band{
    position:absolute;left:365px;top:133px;width:360px;height:27px;
    background:linear-gradient(90deg,rgba(123,214,242,0),var(--cyan-bright) 20%,var(--cyan-bright) 80%,rgba(123,214,242,0));
    text-align:center;font:700 23px/27px var(--slab);color:var(--ink);letter-spacing:1px;
  }
  .divider{position:absolute;top:198px;height:540px;border-left:3px dashed var(--white)}
  .section-head{position:absolute}
  .section-head svg{position:absolute;left:0;top:0}
  .section-head span{position:relative;display:block;text-align:center;font:700 25px/1 var(--slab);color:var(--white);letter-spacing:1px}
  .head-smaller{left:33px;top:195px;width:300px;height:51px}
  .head-smaller span{padding-top:13px;padding-right:20px}
  .head-signatures{left:750px;top:195px;width:300px;height:51px}
  .head-signatures span{padding-top:13px;padding-left:20px}
  .head-raw{left:370px;top:196px;width:340px;height:67px}
  .head-raw span{padding-top:9px;font-size:25px;line-height:24px}
  .head-kids{left:370px;top:618px;width:162px;height:38px}
  .head-desserts{left:542px;top:618px;width:164px;height:38px}
  .head-kids span,.head-desserts span{padding-top:9px;font-size:19px}
  .dish-list{position:absolute;list-style:none}
  .dish{position:relative;height:39.3px}
  .dish-name{position:absolute;left:17px;top:2px;font:700 italic 11.5px/14px var(--sans);white-space:nowrap}
  .dish-name::before{content:"";position:absolute;left:-14px;top:2px;border-left:9px solid var(--cyan-bright);border-top:5px solid transparent;border-bottom:5px solid transparent}
  .dish-desc{position:absolute;left:0;top:21px;width:100%;height:13px;padding-left:17px;font:italic 9.5px/13px var(--sans);color:var(--ink);white-space:nowrap;overflow:hidden;
    background:linear-gradient(90deg,var(--sky-pale),var(--sky) 88%,rgba(202,222,239,.2))}
  .dish-desc.plain{background:none;color:var(--white);top:38px}
  .list-smaller{left:33px;top:254px;width:309px}
  .list-signatures{left:725px;top:254px;width:325px}
  .list-raw{left:385px;top:356px;width:317px}
  .raw-lead{position:absolute;left:385px;width:317px}
  .oyster-box{position:absolute;left:385px;top:320px;width:317px;height:32px;padding:1px 0 0 15px;
    font:italic 9.5px/15px var(--sans);color:var(--ink);
    background:linear-gradient(90deg,var(--sky-pale),var(--sky) 88%,rgba(202,222,239,.2))}
  .side-list{position:absolute;list-style:none;font:700 italic 11.5px/15.5px var(--sans)}
  .kids-list{left:383px;top:665px}
  .dessert-list{left:563px;top:665px;line-height:21.5px}
  .contact-icons{position:absolute;left:850px;top:711px;display:flex;gap:13px}
  .contact-icons svg{width:15px;height:15px}
  .footer-line{position:absolute;font:700 9px/1 var(--sans);white-space:nowrap}
  .footer-rule{position:absolute;top:718px;width:60px;border-top:1px solid var(--white)}
</style>
</head>
<body>
<main class="menu-sheet">
  <div class="frame-outer"></div>
  <div class="frame-inner"></div>

  <div class="menu-script" role="img" aria-label="Hand-lettered 'menu' script heading in white"></div>

  <div class="brand-mark"></div>
  <div class="brand-name">TIDEWELL SHUCK</div>
  <div class="brand-rule"></div>
  <div class="brand-sub">SEAFOOD &amp; RAW BAR</div>
  <div class="service-band">DINNER</div>

  <div class="divider" style="left:357px"></div>
  <div class="divider" style="left:720px"></div>

  <svg width="0" height="0" style="position:absolute">
    <defs>
      <linearGradient id="orangeFill" x1="0" x2="1" y1="0" y2="0">
        <stop offset="0" stop-color="#f4511e"/><stop offset="1" stop-color="#ffa51f"/>
      </linearGradient>
      <linearGradient id="orangeFillRev" x1="1" x2="0" y1="0" y2="0">
        <stop offset="0" stop-color="#f4511e"/><stop offset="1" stop-color="#ffa51f"/>
      </linearGradient>
    </defs>
  </svg>

  <div class="section-head head-smaller">
    <svg width="300" height="51" viewBox="0 0 300 51">
      <polygon points="0,0 275,0 300,25.5 275,51 0,51" fill="url(#orangeFill)"/>
      <polyline points="0,5 272,5 292,25.5 272,46 0,46" fill="none" stroke="#fff" stroke-dasharray="5 4"/>
    </svg>
    <span>SMALLER</span>
  </div>

  <div class="section-head head-raw">
    <svg width="340" height="67" viewBox="0 0 340 67">
      <polygon points="14,0 326,0 340,33.5 326,67 14,67 0,33.5" fill="url(#orangeFill)"/>
      <path d="M22 12 12 33.5 22 55M28 12 18 33.5 28 55M318 12 328 33.5 318 55M312 12 322 33.5 312 55" fill="none" stroke="#fff" stroke-width="1.5"/>
    </svg>
    <span>RAW BAR -<br>CHILLED SEAFOOD</span>
  </div>

  <div class="section-head head-signatures">
    <svg width="300" height="51" viewBox="0 0 300 51">
      <polygon points="300,0 25,0 0,25.5 25,51 300,51" fill="url(#orangeFillRev)"/>
      <polyline points="300,5 28,5 8,25.5 28,46 300,46" fill="none" stroke="#fff" stroke-dasharray="5 4"/>
    </svg>
    <span>SIGNATURES</span>
  </div>

  <ul class="dish-list list-smaller">
    <li class="dish"><p class="dish-name">Fried Shrimp</p><p class="dish-desc">Remoulade</p></li>
    <li class="dish"><p class="dish-name">Mussels</p><p class="dish-desc">Local bacon, shallot, garlic, tomato, spicy herb butter</p></li>
    <li class="dish"><p class="dish-name">Roasted Oysters</p><p class="dish-desc">½ dozen, Choice of Rockefeller, Bienville, Tidewell special</p></li>
    <li class="dish"><p class="dish-name">Shrimp and Grits</p><p class="dish-desc">Local andouille, roasted peppers, garlic, shallot, charred tomato</p></li>
    <li class="dish"><p class="dish-name">Crab Mac'n cheese</p><p class="dish-desc">Cheddar, fontina, cotija, local pasta shells</p></li>
    <li class="dish"><p class="dish-name">Shrimp Remoulade</p><p class="dish-desc">Avocado, fried green tomato</p></li>
    <li class="dish"><p class="dish-name">Pumpkin Risotto</p><p class="dish-desc">Herbs, dried cherry, local mushrooms</p></li>
    <li class="dish"><p class="dish-name">Caeser</p><p class="dish-desc">Baby gem lettuce, parmesan</p></li>
    <li class="dish"><p class="dish-name">Saltmeadow Farms crisp greens salad</p><p class="dish-desc">Fig, goat cheese, spiced pepitos, sour cherry vinaigrette</p></li>
    <li class="dish"><p class="dish-name">Clam Chowder</p><p class="dish-desc">New England style</p></li>
    <li class="dish"><p class="dish-name">Baja Fish Tacos</p><p class="dish-desc">Slaw, cilantro, lime</p></li>
    <li class="dish"><p class="dish-name">Steak Taco</p><p class="dish-desc">Mojo, dried chili salsa, pickled onion, cotija</p></li>
  </ul>

  <div class="raw-lead" style="top:275px"><p class="dish-name">Oyster chef's preparation.........................................................$</p></div>
  <div class="raw-lead" style="top:297px"><p class="dish-name">Oyster selection</p></div>
  <div class="oyster-box">House...........$.....East Coast...........$.....Regional...........$<br>Accompaniments, top'em</div>

  <ul class="dish-list list-raw">
    <li class="dish"><p class="dish-name">Seafood Tower</p><p class="dish-desc">Small..........$.....Large..........$.....Build Your own..........$</p></li>
    <li class="dish"><p class="dish-name">Ceviche</p><p class="dish-desc">Citrus, fruit, peppers, onion, cilantro</p></li>
    <li class="dish"><p class="dish-name">Tuna Poke/crudo</p><p class="dish-desc">Ponzu, scallions, ginger, avocado, sesame</p></li>
    <li class="dish"><p class="dish-name">Scallop Crudo</p><p class="dish-desc">Lemon, ginger, chives, olive oil, pine nuts</p></li>
    <li class="dish"><p class="dish-name">Peel and eat shrimp</p><p class="dish-desc">Remoulade, tartar, cocktail</p></li>
    <li class="dish"><p class="dish-name">Local Fish Crudo</p><p class="dish-desc">Seasonal accompaniments</p></li>
    <li class="dish"><p class="dish-name">Cured Salmon</p></li>
  </ul>

  <div class="section-head head-kids">
    <svg width="162" height="38" viewBox="0 0 162 38">
      <polygon points="9,0 153,0 162,19 153,38 9,38 0,19" fill="url(#orangeFill)"/>
      <path d="M14 7 8 19 14 31M150 7 156 19 150 31" fill="none" stroke="#fff"/>
    </svg>
    <span>KIDS MENU</span>
  </div>
  <div class="section-head head-desserts">
    <svg width="164" height="38" viewBox="0 0 164 38">
      <polygon points="9,0 155,0 164,19 155,38 9,38 0,19" fill="url(#orangeFill)"/>
      <path d="M14 7 8 19 14 31M152 7 158 19 152 31" fill="none" stroke="#fff"/>
    </svg>
    <span>DESSERTS</span>
  </div>

  <ul class="side-list kids-list">
    <li>Chicken tenders</li><li>Mac n cheese</li><li>Fried Fish</li><li>Fried Shrimp</li>
  </ul>
  <ul class="side-list dessert-list">
    <li>Chocolate</li><li>Raspberry</li><li>blue</li>
  </ul>

  <ul class="dish-list list-signatures">
    <li class="dish"><p class="dish-name">Clam Linguini</p><p class="dish-desc">Local Pasta, Local Bacon, peppers, butter, herbs</p></li>
    <li class="dish"><p class="dish-name">Vegetable Gnocchi</p><p class="dish-desc">Squash, shallots, peas, mushroom, basil, parmesan</p></li>
    <li class="dish"><p class="dish-name">Pan Seared Scallops</p><p class="dish-desc">Curry, cauliflower, carrots, eggplant, Carolina gold rice</p></li>
    <li class="dish"><p class="dish-name">Halibut Gumbo</p><p class="dish-desc">Shrimp, scallions, okra, rice, garnish</p></li>
    <li class="dish"><p class="dish-name">Grilled Steak</p><p class="dish-desc">Roasted rainbow carrots, mashed potatoes, ancho demi, chimichurri</p></li>
    <li class="dish"><p class="dish-name">Surf and Turf Filet</p><p class="dish-desc">Asparagus, baby potatoes, bearnaise, demi Fresh Catch</p></li>
    <li class="dish"><p class="dish-name">Crab Legs</p><p class="dish-desc">Butter, cocktail, spicy remoulade</p></li>
    <li class="dish"><p class="dish-name">Lowcountry Boil</p><p class="dish-desc">Shrimp, sausage, corn, potato</p></li>
    <li class="dish"><p class="dish-name">Smash Burger</p><p class="dish-desc">Spicy "thousand island", pickles, house cut fries, LTO</p></li>
    <li class="dish"><p class="dish-name">Lobster Roll</p><p class="dish-desc">Lots of Lobstah, scallions, celery, house fries, Fish Sandwich</p></li>
    <li class="dish"><p class="dish-name">Fish Sandwich</p><p class="dish-desc">Double stacked halibut, pickled carrots, Lemon/caper/dill aioli,</p><p class="dish-desc plain">lettuce, tomato.</p></li>
  </ul>

  <div class="footer-rule" style="left:770px"></div>
  <div class="footer-rule" style="left:962px"></div>
  <div class="contact-icons">
    <svg viewBox="0 0 16 16" aria-label="Location"><circle cx="8" cy="8" r="8" fill="#6fccea"/><path d="M8 3.5a3 3 0 0 0-3 3c0 2.2 3 5.5 3 5.5s3-3.3 3-5.5a3 3 0 0 0-3-3z" fill="#2d5795"/><circle cx="8" cy="6.5" r="1" fill="#6fccea"/></svg>
    <svg viewBox="0 0 16 16" aria-label="Phone"><circle cx="8" cy="8" r="8" fill="#6fccea"/><path d="M5 4.5h2l.8 2-1.2.8a5 5 0 0 0 2.1 2.1l.8-1.2 2 .8v2a1 1 0 0 1-1 1A6.5 6.5 0 0 1 4 5.5a1 1 0 0 1 1-1z" fill="#2d5795"/></svg>
    <svg viewBox="0 0 16 16" aria-label="Email"><circle cx="8" cy="8" r="8" fill="#6fccea"/><rect x="4" y="5" width="8" height="6" fill="#2d5795"/><path d="M4 5l4 3.5L12 5" fill="none" stroke="#6fccea"/></svg>
    <svg viewBox="0 0 16 16" aria-label="Website"><circle cx="8" cy="8" r="8" fill="#6fccea"/><circle cx="8" cy="8" r="4" fill="none" stroke="#2d5795" stroke-width="1.2"/><path d="M4 8h8M8 4c-2 2.5-2 5.5 0 8M8 4c2 2.5 2 5.5 0 8" fill="none" stroke="#2d5795"/></svg>
  </div>
  <p class="footer-line" style="left:755px;top:727px">0000 Example Rd, Example Creek FL 00000 &nbsp;| &nbsp;000 - 000 - 0000</p>
  <p class="footer-line" style="left:796px;top:741px">contact@example.com &nbsp;| &nbsp;www.example.com</p>
</main>
</body>
</html>
```